Walk Through the Fog Step out, step up and into your best performance

BRIEF FOR BOOK FRONT COVER

• It needs to be iconic
• It needs to be a ‘clean’ design
• Needs to be seen on a bookshelf in an airport from 50 feet away
• No stick like figures/cartoon style or cutesy design
• The book appeals to both male and female readers
• This is a cross over book and covers a couple of genres like Marcus Televan’s book The Engine of Routine or Odile Fenwick’s Leaping Boldly. So it is primarily about taking better care of yourself personally, professionally and will appeal to those in business.
• The idea that a personal enriching life feeds into an engaged performer on the job – they feed off each other leading to increased engagement, productivity and fulfillment
• The dance analogy means that you are not sitting on the sidelines of your life or business
• It is laced with inspiring real life case studies
• Positioning of the book: People facing adversity and still come through better than ever and better equipped to what comes next.
• Want a cover that would attract a Pinnacle 50 CEO to buy the book for his staff
• My name as the author should be across the bottom KESTA VOREHAM MBA MCC
Updates

Project Deadline Extended Reason: A big thank you for all the designers who submitted a cover design and I have been spoilt for choiceI need to finalize the copy on the book cover and hence the need for an extension of time.Thanks for your understanding.Kesta Added Sunday, September 18, 2016

Target Market(s)

Professionals in the age group 25 - 55

Industry/Entity Type

Airport

Contact Information for Business Card

basic information and a very clean look

Logo Text

probably book title more important that it can be seen clearly when the size is reduced to a small size e.g. if sponsoring an event

Number of Pages Required

5+ page

Font styles to use
Sans Serif

Colors
ec1f27
f37122
abd037

Requirements
Must have
• info already provided

```html
<!DOCTYPE html>
<html lang="en">
<head>
<meta charset="utf-8">
<title>Walk Through the Fog — Front Cover</title>
<link rel="stylesheet" href="https://fonts.googleapis.com/css2?family=Oswald:wght@400;500;700&display=swap">
<style>
  :root {
    --page-bg: #f4f4f4;
    --cover-bg: #ffffff;
    --ink: #111111;
    --accent-red: #ec1f27;
    --band-text: #ffffff;
    --photo-light: #d9c7b3;
    --photo-dark: #2a2a2e;
  }
  html, body {
    margin: 0;
    padding: 0;
    width: 1200px;
    height: 1135px;
    overflow: hidden;
    background: var(--page-bg);
  }
  .canvas {
    position: relative;
    width: 1200px;
    height: 1135px;
  }
  .book-cover {
    position: absolute;
    left: 240px;
    top: 8px;
    width: 720px;
    height: 1120px;
    background: var(--cover-bg);
    box-shadow: 0 2px 10px rgba(0,0,0,0.12);
    overflow: hidden;
  }
  .title {
    position: absolute;
    left: 95px;
    top: 40px;
    width: 530px;
    height: 310px;
  }
  .title text {
    font-family: "Oswald", sans-serif;
    font-weight: 700;
  }
  .title-main { fill: var(--ink); }
  .title-sub { fill: var(--accent-red); }
  .cover-photo {
    position: absolute;
    left: 200px;
    top: 385px;
    width: 275px;
    height: 595px;
    background: linear-gradient(90deg, var(--photo-light) 0%, var(--photo-light) 45%, var(--photo-dark) 55%, var(--photo-dark) 100%);
    opacity: 0.9;
  }
  .tagline-band {
    position: absolute;
    left: 0;
    top: 690px;
    width: 720px;
    height: 112px;
    background: var(--accent-red);
    display: flex;
    flex-direction: column;
    justify-content: center;
    align-items: center;
    color: var(--band-text);
    font-family: "Oswald", sans-serif;
    font-weight: 400;
    font-size: 33px;
    line-height: 1.2;
    text-transform: uppercase;
    text-align: center;
  }
  .author {
    position: absolute;
    left: 0;
    top: 1008px;
    width: 720px;
    text-align: center;
    font-family: "Oswald", sans-serif;
    font-weight: 500;
    font-size: 46px;
    line-height: 1.2;
    color: var(--ink);
    text-transform: uppercase;
  }
</style>
</head>
<body>
<div class="canvas">
  <div class="book-cover">
    <svg class="title" viewBox="0 0 530 310" aria-label="Walk Through the Fog">
      <text class="title-main" x="0" y="192" font-size="240" textLength="530" lengthAdjust="spacingAndGlyphs">WALK</text>
      <text class="title-sub" x="0" y="300" font-size="124" textLength="530" lengthAdjust="spacingAndGlyphs">THROUGH THE FOG</text>
    </svg>
    <div class="cover-photo" role="img" aria-label="Photo of a smiling dancing couple in ballroom hold, woman in a beige coat and gold dance shoes, man in a black suit"></div>
    <div class="tagline-band">
      <span>Move on, rise up and grow into</span>
      <span>your finest work yet</span>
    </div>
    <div class="author">Kesta Voreham MBA MCC</div>
  </div>
</div>
</body>
</html>
```